New business card design for Maplewood Ridge Optometry Clinic

We need a new business card design using our existing logo (uploaded). Please do not include eyes, eye exam charts or beaches, water, sand. The logo I uploaded shows our colors of green and blue, but we are open to seeing it in black OR white. We would like to see something modern and fresh. It will need to be 2 sided. On the front we will need to be able to put a doctors name, for example-Dr Clara Venhuisen and Associates. We will need to be able to change the name to other doctors names when we send for printing. The back of the card should list the following: 1748 Tarrow St, Linden Falls (P)705-555-0183 (E) info@mroc-example.ca www.mroc-example.ca. "We are welcoming new patients" and a line for the appointment date and time. I have uploaded the back of a card to give an example

```html
<!DOCTYPE html>
<html lang="en">
<head>
<meta charset="utf-8">
<title>Maplewood Ridge Optometry Clinic – Business Card</title>
<link rel="stylesheet" href="https://fonts.googleapis.com/css2?family=Montserrat:wght@700;800&family=Lato:wght@400;700&family=Crimson+Text:wght@400&display=swap">
<style>
  :root {
    --blue: #2f4fa8;
    --green: #1f9a48;
    --ink: #555a60;
    --rule: #6b6f74;
    --paper: #ffffff;
    --backdrop: #e4e6e9;
  }
  * { box-sizing: border-box; margin: 0; padding: 0; }
  html, body { width: 1200px; height: 952px; overflow: hidden; }
  body {
    background: var(--backdrop);
    position: relative;
    font-family: "Lato", sans-serif;
  }
  .card {
    position: absolute;
    width: 540px;
    height: 309px;
    background: var(--paper);
    overflow: hidden;
    box-shadow: 0 6px 18px rgba(0,0,0,0.12);
  }
  .card--front { left: 610px; top: 110px; }
  .card--back  { left: 50px;  top: 530px; }

  /* Front */
  .tab {
    position: absolute;
    background: var(--green);
    border-radius: 12px;
  }
  .tab--top    { left: -20px; top: 22px; width: 110px; height: 72px; }
  .tab--bottom { right: -20px; bottom: 22px; width: 130px; height: 72px; }

  .brand {
    display: flex;
    align-items: center;
    gap: 10px;
    font-family: "Montserrat", sans-serif;
    font-weight: 800;
    color: var(--blue);
    white-space: nowrap;
  }
  .brand__dot {
    border-radius: 50%;
    background: var(--green);
    flex: none;
  }
  .card--front .brand {
    position: absolute;
    left: 50%; top: 50%;
    transform: translate(-50%, -50%);
    font-size: 22px;
  }
  .card--front .brand__dot { width: 22px; height: 22px; }

  /* Back */
  .headline {
    position: absolute;
    left: 0; right: 0; top: 26px;
    text-align: center;
    font-family: "Montserrat", sans-serif;
    font-weight: 800;
    font-size: 21px;
    letter-spacing: 0.5px;
    color: var(--green);
  }
  .card--back .brand {
    position: absolute;
    left: 50%; top: 68px;
    transform: translateX(-50%);
    font-size: 17px;
  }
  .card--back .brand__dot { width: 16px; height: 16px; }

  .contacts {
    position: absolute;
    left: 0; right: 0; top: 110px;
    display: flex;
    justify-content: center;
    gap: 18px;
    font-size: 13px;
    color: var(--ink);
  }
  .contact { display: flex; align-items: center; gap: 5px; }
  .contact svg { width: 14px; height: 14px; flex: none; }
  .address {
    position: absolute;
    left: 0; right: 0; top: 134px;
    text-align: center;
    font-size: 14px;
    color: var(--ink);
  }

  .field {
    position: absolute;
    font-family: "Crimson Text", serif;
    font-size: 15px;
    display: flex;
    align-items: flex-end;
    gap: 8px;
  }
  .field__rule { flex: 1; border-bottom: 1.5px solid var(--rule); height: 1px; margin-bottom: 4px; }
  .field--doctor { left: 32px; right: 32px; top: 184px; color: var(--blue); }
  .field--date   { left: 32px; width: 220px; top: 236px; color: var(--green); }
  .field--time   { left: 280px; right: 32px; top: 236px; color: var(--green); }
</style>
</head>
<body>

  <section class="card card--front" aria-label="Card front">
    <div class="tab tab--top"></div>
    <div class="tab tab--bottom"></div>
    <div class="brand">
      <span class="brand__dot"></span>
      <span class="brand__name">Maplewood Ridge Optometry Clinic</span>
    </div>
  </section>

  <section class="card card--back" aria-label="Card back">
    <h1 class="headline">WE ARE WELCOMING NEW PATIENTS</h1>
    <div class="brand">
      <span class="brand__dot"></span>
      <span class="brand__name">Maplewood Ridge Optometry Clinic</span>
    </div>

    <div class="contacts">
      <span class="contact">
        <svg viewBox="0 0 14 14" aria-hidden="true"><rect width="14" height="14" rx="3" fill="#2f4fa8"/><path d="M4.3 3.2l1.6 1.9-.8 1c.6 1.2 1.5 2.1 2.7 2.7l1-.8 1.9 1.6-.9 1.3C6.7 10.6 3.4 7.3 3.1 4.1z" fill="#fff"/></svg>
        705-555-0183
      </span>
      <span class="contact">
        <svg viewBox="0 0 14 14" aria-hidden="true"><rect width="14" height="14" rx="3" fill="#2f4fa8"/><rect x="3" y="4" width="8" height="6" fill="none" stroke="#fff" stroke-width="1.2"/><path d="M3 4l4 3.5L11 4" fill="none" stroke="#fff" stroke-width="1.2"/></svg>
        info@mroc-example.ca
      </span>
      <span class="contact">
        <svg viewBox="0 0 14 14" aria-hidden="true"><rect width="14" height="14" rx="3" fill="#2f4fa8"/><circle cx="7" cy="7" r="3.8" fill="none" stroke="#fff" stroke-width="1.1"/><path d="M3.2 7h7.6M7 3.2c-1.6 2.2-1.6 5.4 0 7.6M7 3.2c1.6 2.2 1.6 5.4 0 7.6" fill="none" stroke="#fff" stroke-width="0.9"/></svg>
        www.mroc-example.ca
      </span>
    </div>
    <p class="address">1748 Tarrow St, Linden Falls</p>

    <div class="field field--doctor"><span>Doctors Name</span><span class="field__rule"></span></div>
    <div class="field field--date"><span>Date</span><span class="field__rule"></span></div>
    <div class="field field--time"><span>Time</span><span class="field__rule"></span></div>
  </section>

</body>
</html>
```